Pricing sheet For Acupuncture Clinic - Remake Attached Work

Right Now I have 4 pricing sheets that look very disorganized. They are for 4 different options of services I offer with 3 different options to pay for each service (pay each time you come in, prepaid package, or a monthly option). People get confused from this outline so looking to make this easier to understand and better looking. You can reorganize the pricing as you see fit as long as it makes sense. (ex: using columns or rows or a graph) These images are going to be made into standard sized posters (i think that is 5 feet by 7 feet?)

Instead of designing all 4 of the attached files below you can choose 1 of them to show your example of work. I will assume that style will apply to all 4 sheets if I choose your work - also need 1 sheet that can print out on paper that will show all treatments on front and back of paper.

Thank you
Milo

Target Market(s)

Spa Industry

Industry/Entity Type

Clinic

Font styles to use
Serif
Sans Serif
Decorative
Script

Colors
33a6d7
ffffff
000000

Requirements
Nice to have
• clean - organized -
Should not have
• pictures of acupuncture needles. anything sharp. anything that might make people feel afraid of getting the treatments or look painful

```html
<!DOCTYPE html>
<html lang="en">
<head>
<meta charset="utf-8">
<title>Body Acupuncture – Pricing Sheet</title>
<link rel="stylesheet" href="https://fonts.googleapis.com/css2?family=Bebas+Neue&family=Open+Sans:wght@300;400;600;700&family=Roboto+Condensed:wght@400&display=swap">
<style>
  :root {
    --backdrop: #5d5f5f;
    --brand-blue: #33bfd8;
    --ink: #1a1a1a;
    --white: #ffffff;
    --dark-center: #5c5c5c;
    --dark-edge: #1c1c1c;
    --strip: #a9a9a9;
  }
  * { margin: 0; padding: 0; box-sizing: border-box; }
  html, body { width: 997px; height: 1200px; overflow: hidden; background: var(--backdrop); }
  .canvas { position: relative; width: 997px; height: 1200px; }
  .sheet {
    position: absolute; left: 135px; top: 94px; width: 726px; height: 1008px;
    background: var(--white); overflow: hidden;
  }
  .hero-photo {
    position: absolute; left: 0; top: 0; width: 726px; height: 392px;
    background:
      radial-gradient(ellipse at 62% 72%, #b0755a 0%, #8d5a44 35%, transparent 65%),
      radial-gradient(ellipse at 75% 15%, #a87058 0%, transparent 50%),
      linear-gradient(180deg, #c9c6c3 0%, #8f8a86 55%, #6a625c 100%);
  }
  .photo-rule { position: absolute; left: 0; top: 392px; width: 726px; height: 12px; background: var(--strip); }
  .brand-tile {
    position: absolute; left: 38px; top: 35px; width: 175px; height: 143px;
    background: var(--white); display: flex; align-items: center; justify-content: center;
    font-family: "Bebas Neue", sans-serif; color: var(--brand-blue);
    font-size: 30px; line-height: 0.95; text-align: center; letter-spacing: 1px;
  }
  .pricing-panel {
    position: absolute; left: 0; top: 404px; width: 726px; height: 441px;
    background: radial-gradient(ellipse at 50% 45%, var(--dark-center) 0%, #333 45%, var(--dark-edge) 100%);
    color: var(--white);
  }
  .service-title {
    position: absolute; left: 0; top: 20px; width: 100%; text-align: center;
    font-family: "Bebas Neue", sans-serif; font-size: 74px; line-height: 1;
    color: var(--brand-blue); letter-spacing: -0.5px; font-weight: 400;
  }
  .service-benefits {
    position: absolute; left: 0; top: 103px; width: 100%; text-align: center;
    font-family: "Open Sans", sans-serif; font-weight: 300; font-size: 24.5px;
  }
  .plan-card {
    position: absolute; top: 175px; width: 215px; height: 238px;
    border: 3px dotted var(--white); border-radius: 14px;
    text-align: center; font-family: "Open Sans", sans-serif;
  }
  .plan-card--payg { left: 23px; }
  .plan-card--prepaid { left: 256px; }
  .plan-card--autopay { left: 489px; }
  .plan-name {
    margin: 22px 17px 0; padding-bottom: 10px; border-bottom: 2px solid var(--white);
    font-family: "Bebas Neue", sans-serif; font-size: 29px; line-height: 1;
    color: var(--brand-blue); font-weight: 400; white-space: nowrap;
  }
  .plan-note { font-size: 13px; margin-top: 9px; }
  .plan-list { list-style: none; margin-top: 4px; font-size: 17.5px; line-height: 21.5px; }
  .plan-card--prepaid .plan-list { margin-top: 20px; }
  .plan-list li { white-space: nowrap; }
  .plan-price { display: block; color: var(--brand-blue); font-weight: 700; }
  .plan-retail { margin-top: 38px; font-size: 19px; line-height: 23px; }
  .plan-ours { margin-top: 6px; font-size: 19px; line-height: 23px; color: var(--brand-blue); font-weight: 600; }
  .terms {
    position: absolute; left: 0; top: 845px; width: 100%; height: 88px;
    padding-top: 8px; text-align: center;
    font-family: "Roboto Condensed", sans-serif; font-size: 12px; line-height: 18px;
    color: var(--ink); text-transform: uppercase;
  }
  .contact-bar {
    position: absolute; left: 0; top: 933px; width: 100%; height: 75px;
    background: var(--brand-blue); color: var(--white);
    display: flex; align-items: center; justify-content: center; gap: 28px;
    font-family: "Open Sans", sans-serif; font-size: 12.5px;
  }
  .contact-item { display: flex; align-items: center; gap: 7px; }
  .contact-item svg { width: 14px; height: 14px; fill: none; stroke: var(--white); stroke-width: 1.6; }
</style>
</head>
<body>
<div class="canvas">
  <main class="sheet">
    <div class="hero-photo" role="img" aria-label="Photo of relaxed bare feet resting during a treatment session"></div>
    <div class="brand-tile">Harbor Light<br>Acupuncture</div>
    <div class="photo-rule"></div>

    <section class="pricing-panel">
      <h1 class="service-title">Body Acupuncture</h1>
      <p class="service-benefits">Pain, Weight Loss, Hormones, Anxiety, Insomnia, Allergies</p>

      <div class="plan-card plan-card--payg">
        <h2 class="plan-name">Pay As You Go</h2>
        <p class="plan-retail">Retail: $75<br>Treatment</p>
        <p class="plan-ours">Our price: $50<br>Treatment</p>
      </div>

      <div class="plan-card plan-card--prepaid">
        <h2 class="plan-name">Pre-Paid Packages</h2>
        <ul class="plan-list">
          <li>6 Treatments/month<span class="plan-price">$270/month</span></li>
          <li>12 Treatments/Month<span class="plan-price">$480/month</span></li>
          <li>24 Treatments/Month<span class="plan-price">$720/month</span></li>
        </ul>
      </div>

      <div class="plan-card plan-card--autopay">
        <h2 class="plan-name">Monthly Autopay</h2>
        <p class="plan-note">Roll Over - Min 4 Months</p>
        <ul class="plan-list">
          <li>4 Treatments/month<span class="plan-price">$160/month</span></li>
          <li>8 Treatments/Month<span class="plan-price">$240/month</span></li>
          <li>12 Treatments/Month<span class="plan-price">$340/month</span></li>
        </ul>
      </div>
    </section>

    <section class="terms">
      <p>Auto pay unused treatments roll - over - pre-paid package expire after 1 year</p>
      <p>Autopay may be cancelled anytime after 4 months</p>
      <p>Monthly autopay unused treatments</p>
      <p>Will be forfeited 3 months after cancellation</p>
    </section>

    <footer class="contact-bar">
      <span class="contact-item">
        <svg viewBox="0 0 14 14"><path d="M7 13 C3 8 2.5 6.5 2.5 5 A4.5 4.5 0 0 1 11.5 5 C11.5 6.5 11 8 7 13Z" fill="#fff" stroke="none"/><circle cx="7" cy="5" r="1.6" fill="#33bfd8" stroke="none"/></svg>
        2210 Harbor View Road, Bayside, CA 92000
      </span>
      <span class="contact-item">
        <svg viewBox="0 0 14 14"><circle cx="7" cy="7" r="6"/><path d="M5 4.2 L6 6 L5.4 6.8 Q6.3 8.2 7.4 8.7 L8.2 8 L9.9 9 L9.3 10 Q6.5 10.2 4.3 6.3 Q4 5 5 4.2Z" fill="#fff" stroke="none"/></svg>
        (555) 014-2290
      </span>
      <span class="contact-item">
        <svg viewBox="0 0 14 14"><circle cx="7" cy="7" r="6"/><ellipse cx="7" cy="7" rx="2.6" ry="6"/><path d="M1 7 H13 M2 4 H12 M2 10 H12"/></svg>
        harborlightacupuncture.com
      </span>
    </footer>
  </main>
</div>
</body>
</html>
```